"Rodrigo Velvet" Business Card

Friends

My name is "Rodrigo Velvet" and I need your help! I need a new business card for my personal use.

As background, "Rodrigo Velvet" is actually an alias that I use when I meet women. Please use your creative skills to create an amazing business card for me to use!

In addition to including my name and contact details (see the "Must Have" section), you may wish to add a catchphrase or a title if you think it would help me :)

For background, please see:

http://www.dailyripplenews.com/2013/07/23/marcus-pell-rodrigo-velvet_n_8152704.html

Looking forward to seeing what you can do for me.

Hugs and kisses,

Rodrigo Velvet [courtesy of ArtQuarry]

Target Market(s)

Adult women in New York City...or anywhere really.

Industry/Entity Type

Business

Requirements
Must have
• Please include the following details:

Rodrigo Velvet
P: +1-555-4VELVET
E: secrets@rodrigovelvet.example
Nice to have
• You might include a catchphrase, like "Velvet is my surname But you can call me Mr Hardbody".

Or perhaps a title, like "Rodrigo Velvet, Head of Sexy Times".

You're creative...I will leave the details to you my friends.
Should not have
• Any references to my actual name...because then, what's the point in using an alias?

```html
<!DOCTYPE html>
<html lang="en">
<head>
<meta charset="utf-8">
<title>Rodrigo Velvet Business Card</title>
<link rel="stylesheet" href="https://fonts.googleapis.com/css2?family=Great+Vibes&family=Comfortaa:wght@300;400&display=swap">
<style>
  :root {
    --backdrop: #2a2a2c;
    --card-white: #ffffff;
    --rose: #e23c68;
    --rose-deep: #c42d58;
    --plum: #8a4fa8;
    --ink-light: #ffffff;
    --heart-blush: #f7c9d6;
  }
  html, body {
    margin: 0;
    padding: 0;
    width: 1200px;
    height: 900px;
    overflow: hidden;
    background: var(--backdrop);
  }
  .canvas {
    position: relative;
    width: 1200px;
    height: 900px;
  }
  .card {
    position: absolute;
    left: 100px;
    width: 1000px;
    height: 360px;
    filter: drop-shadow(0 10px 18px rgba(0,0,0,0.45));
  }
  .card--back { top: 50px; }
  .card--front { top: 480px; }
  .card-name {
    font-family: "Great Vibes", cursive;
    font-size: 64px;
  }
  .card-name--plum { fill: var(--plum); }
  .card-name--light { fill: var(--ink-light); font-size: 50px; }
  .catchphrase {
    font-family: "Comfortaa", sans-serif;
    font-weight: 300;
    font-size: 28px;
    fill: var(--ink-light);
    letter-spacing: 1px;
  }
  .contact-line {
    font-family: "Comfortaa", sans-serif;
    font-weight: 300;
    font-size: 25px;
    fill: var(--ink-light);
    letter-spacing: 1.5px;
  }
  .contact-icon {
    fill: none;
    stroke: var(--ink-light);
    stroke-width: 3;
    stroke-linejoin: round;
  }
</style>
</head>
<body>
<main class="canvas">

  <svg class="card card--back" viewBox="0 0 1000 360" aria-label="Card back with name and catchphrase">
    <defs>
      <clipPath id="lip-shape-back">
        <path d="M0,150 C60,150 120,30 260,30 C360,30 420,90 500,90 C580,90 640,30 740,30 C880,30 940,150 1000,150 L1000,360 L0,360 Z"/>
      </clipPath>
      <linearGradient id="rose-band" x1="0" y1="0" x2="1" y2="1">
        <stop offset="0" stop-color="var(--rose)"/>
        <stop offset="1" stop-color="var(--rose-deep)"/>
      </linearGradient>
      <radialGradient id="heart-field" cx="0.5" cy="0.55" r="0.7">
        <stop offset="0" stop-color="#ffffff"/>
        <stop offset="1" stop-color="#fdf1f5"/>
      </radialGradient>
    </defs>
    <g clip-path="url(#lip-shape-back)">
      <rect class="heart-field" x="0" y="0" width="1000" height="250" fill="url(#heart-field)" role="img" aria-label="White field scattered with small pink hearts"/>
      <rect class="rose-band" x="0" y="250" width="1000" height="110" fill="url(#rose-band)"/>
    </g>
    <text class="card-name card-name--plum" x="500" y="205" text-anchor="middle">Rodrigo Velvet</text>
    <text class="catchphrase" x="500" y="295" text-anchor="middle">Velvet is my surname But you can call me</text>
    <text class="catchphrase" x="500" y="333" text-anchor="middle">“Mr Hardbody”</text>
  </svg>

  <svg class="card card--front" viewBox="0 0 1000 360" aria-label="Card front with name and contact details">
    <defs>
      <linearGradient id="rose-face" x1="0" y1="0" x2="1" y2="1">
        <stop offset="0" stop-color="#ea4470"/>
        <stop offset="1" stop-color="var(--rose-deep)"/>
      </linearGradient>
    </defs>
    <path class="card-face" fill="url(#rose-face)" d="M0,150 C60,150 120,30 260,30 C360,30 420,90 500,90 C580,90 640,30 740,30 C880,30 940,150 1000,150 L1000,360 L0,360 Z"/>
    <text class="card-name card-name--light" x="36" y="235">“Rodrigo Velvet”</text>

    <g class="contact-phone">
      <rect class="contact-icon" x="412" y="180" width="26" height="40" rx="5"/>
      <line class="contact-icon" x1="418" y1="212" x2="432" y2="212"/>
      <text class="contact-line" x="462" y="210">+1-555-4VELVET</text>
    </g>
    <g class="contact-email">
      <rect class="contact-icon" x="405" y="264" width="38" height="26" rx="2"/>
      <polyline class="contact-icon" points="405,266 424,281 443,266"/>
      <text class="contact-line" x="462" y="286" textLength="500" lengthAdjust="spacingAndGlyphs">secrets@rodrigovelvet.example</text>
    </g>
  </svg>

</main>
</body>
</html>
```